Maplerise Trading Inc. needs an innovative idea for letterhead and visiting cards.

Maplerise Trading Inc. is a Canadian brand since 2007. It is a renown dealer of kids and office furniture locally. Moreover, exporting electric fixtures e.g. switches, LED's, down-lights etc. to Middle East and Africa. We have initiated a number of steps including re-branding, to boost our export in 2020. We have successfully designed our new logo a few months ago through 'Artfolio' and now we are looking for an innovative idea for a letterhead.
Some key points:
• Red, black and white are the three colors used in all our packaging and furniture. (grey is optional)
• Shouldn’t be too wide.
• Use of watermark is preferable.
• You can visit our North American site at www.mapleriseinc.com. Export website of the company will be launched soon. www.mapleriseinc.ca
• Same letterhead will be used locally and internationally.
• Our new logo and sample packaging is attached.

```html
<!DOCTYPE html>
<html lang="en">
<head>
<meta charset="utf-8">
<title>Maplerise Trading Inc. — Letterhead</title>
<link href="https://fonts.googleapis.com/css2?family=Roboto:wght@400;500&display=swap" rel="stylesheet">
<style>
  :root {
    --backdrop: #e4e4e4;
    --paper: #ffffff;
    --brand-red: #c8202b;
    --ink: #3a3a3a;
    --bar-grey: #555657;
    --bar-text: #f2f2f2;
    --watermark: #f0f0f0;
    --muted: #6a6a6a;
  }
  * { box-sizing: border-box; margin: 0; padding: 0; }
  html, body {
    width: 1200px; height: 905px; overflow: hidden;
    background: var(--backdrop);
    font-family: "Roboto", Arial, sans-serif;
  }
  .letterhead {
    position: absolute;
    left: 310px; top: 42px;
    width: 580px; height: 821px;
    background: var(--paper);
    box-shadow: 0 4px 18px rgba(0,0,0,0.12);
  }
  .brand {
    position: absolute; left: 40px; top: 38px;
    display: flex; align-items: center; gap: 10px;
  }
  .brand-square {
    width: 30px; height: 30px; background: var(--brand-red);
  }
  .brand-text { display: flex; flex-direction: column; }
  .brand-name {
    font-size: 17px; font-weight: 500; color: var(--ink);
    letter-spacing: 0.5px; line-height: 1.1;
  }
  .brand-tagline {
    font-size: 7px; color: var(--muted); margin-top: 3px; letter-spacing: 0.3px;
  }
  .watermark {
    position: absolute; left: 170px; top: 250px;
    width: 240px; height: 200px;
    background: var(--watermark);
    border-radius: 6px;
  }
  .address {
    position: absolute; right: 40px; bottom: 72px;
    font-size: 9px; color: var(--ink);
  }
  .contact-bar {
    position: absolute; left: 40px; right: 40px; bottom: 38px;
    height: 24px; background: var(--bar-grey);
    display: flex; align-items: center; gap: 26px;
    padding: 0 14px;
    font-size: 9px; color: var(--bar-text);
  }
  .contact-item { display: flex; align-items: center; gap: 6px; }
  .contact-item svg { width: 10px; height: 10px; fill: var(--bar-text); }
  .edge-line {
    position: absolute; left: 0; right: 0; bottom: 0;
    height: 4px; background: var(--brand-red);
  }
</style>
</head>
<body>
  <main class="letterhead">
    <header class="brand">
      <span class="brand-square"></span>
      <div class="brand-text">
        <span class="brand-name">Maplerise Trading</span>
        <span class="brand-tagline">Furniture &amp; fixtures since 2007</span>
      </div>
    </header>

    <div class="watermark" role="img" aria-label="Faint brand watermark in the centre of the page"></div>

    <footer>
      <p class="address">48 Birchfield Ave, Unit 210, Oakridge, ON L0A 2B7</p>
      <div class="contact-bar">
        <span class="contact-item">
          <svg viewBox="0 0 10 10" aria-hidden="true"><path d="M2 0.5 L4 2.5 L3 3.8 Q4 6 6.2 7 L7.5 6 L9.5 8 L8 9.5 Q4 9.5 0.5 2 Z"/></svg>
          +1 (888) 555-0147
        </span>
        <span class="contact-item">
          <svg viewBox="0 0 10 10" aria-hidden="true"><path d="M0.5 2 H9.5 V8 H0.5 Z M1 2.5 L5 5.5 L9 2.5" stroke="#555657" stroke-width="0.8"/></svg>
          info@mapleriseinc.com
        </span>
        <span class="contact-item">
          <svg viewBox="0 0 10 10" aria-hidden="true"><circle cx="5" cy="5" r="4.5"/></svg>
          www.mapleriseinc.com
        </span>
      </div>
      <div class="edge-line"></div>
    </footer>
  </main>
</body>
</html>
```